Heron Accord Business Card

Need a business card for my nonprofit, Heron Accord Inc. Heron Accord is a conflict resolution practice that offers services that help people resolve problems peacefully.

Got Conflict? Try Conflict Coaching. Initial consultation is complimentary

Marisol Daventry-Kuhl, PhD
Heron Accord Inc.
www.heronaccord-example.org
E: info@heronaccord-example.org
P: 555-318-4927

Would like the attached logo on it, as well as our slogan, which is Finding Calm Around the RoomĀ®

```html
<!DOCTYPE html>
<html lang="en">
<head>
<meta charset="utf-8">
<title>Heron Accord Business Card</title>
<link href="https://fonts.googleapis.com/css2?family=Roboto:wght@400;500&family=Roboto+Condensed:wght@700&display=swap" rel="stylesheet">
<style>
  :root {
    --backdrop: #2a2a2a;
    --card: #f3f2f0;
    --red: #e3313a;
    --gold: #a8841c;
    --gold-light: #d2ac34;
    --rule: #c9c6c0;
    --white: #ffffff;
  }
  * { margin: 0; padding: 0; box-sizing: border-box; }
  html, body { width: 1200px; height: 960px; overflow: hidden; }
  body {
    background: var(--backdrop);
    font-family: "Roboto", Arial, sans-serif;
    position: relative;
  }
  .card {
    position: absolute;
    width: 600px;
    height: 343px;
    background: var(--card);
    border-radius: 22px;
    overflow: hidden;
  }
  .card--front { left: 314px; top: 113px; }
  .card--back { left: 311px; top: 472px; }

  .brand {
    position: absolute;
    left: 56px;
    top: 142px;
    width: 226px;
    display: flex;
    align-items: center;
    justify-content: center;
    gap: 9px;
  }
  .brand__dot {
    width: 13px; height: 13px;
    border-radius: 50%;
    background: var(--red);
    flex: none;
  }
  .brand__name {
    font-size: 23px;
    font-weight: 500;
    letter-spacing: 1px;
    color: var(--gold);
    text-transform: uppercase;
    white-space: nowrap;
  }
  .divider {
    position: absolute;
    left: 300px;
    top: 92px;
    width: 1px;
    height: 136px;
    background: var(--rule);
  }
  .contact {
    position: absolute;
    left: 325px;
    top: 89px;
    color: var(--gold);
    font-size: 14.5px;
    line-height: 18px;
  }
  .contact__name {
    font-family: "Roboto Condensed", Arial, sans-serif;
    font-weight: 700;
    font-size: 19px;
    line-height: 22px;
    color: var(--red);
    margin-bottom: 18px;
  }
  .contact__address { margin-bottom: 14px; }
  .contact__line { display: flex; align-items: center; gap: 7px; line-height: 20px; }
  .contact__line svg { width: 13px; height: 13px; flex: none; }
  .footer-band {
    position: absolute;
    left: 0; bottom: 0;
    width: 600px;
    height: 48px;
    background: linear-gradient(180deg, var(--red) 0%, var(--gold-light) 55%, var(--gold) 100%);
  }
  .website {
    position: absolute;
    right: 73px;
    bottom: 10px;
    color: var(--white);
    font-size: 13.5px;
  }

  .back-copy {
    position: absolute;
    left: 0; right: 0;
    top: 118px;
    text-align: center;
    color: var(--gold);
    font-size: 15px;
    line-height: 19px;
  }
  .social {
    margin: 13px auto 0;
    display: flex;
    align-items: center;
    justify-content: center;
    gap: 4px;
  }
  .social__rule { width: 56px; height: 1px; background: #555; }
  .social__rule--left { margin-right: 2px; }
  .social__rule--right { margin-left: 2px; }
  .social__badge {
    width: 26px; height: 26px;
    border-radius: 50%;
    background: var(--red);
  }
  .slogan {
    margin-top: 10px;
    color: var(--red);
    font-size: 14.5px;
  }
  .slogan sup { font-size: 8px; }
</style>
</head>
<body>
  <section class="card card--front">
    <div class="brand">
      <span class="brand__dot"></span>
      <span class="brand__name">Heron Accord</span>
    </div>
    <div class="divider"></div>
    <div class="contact">
      <p class="contact__name">Marisol Daventry-Kuhl, PhD</p>
      <p class="contact__address">Heron Accord Inc.<br>2941 Cedarbrook Lane<br>Fairhaven, Alaska 30918</p>
      <p class="contact__line">
        <svg viewBox="0 0 24 24" aria-hidden="true"><path fill="#e3313a" d="M6.6 10.8a15.1 15.1 0 0 0 6.6 6.6l2.2-2.2c.3-.3.7-.4 1-.2 1.1.4 2.3.6 3.6.6.6 0 1 .4 1 1V20c0 .6-.4 1-1 1A17 17 0 0 1 3 4c0-.6.4-1 1-1h3.5c.6 0 1 .4 1 1 0 1.3.2 2.5.6 3.6.1.3 0 .7-.2 1z"/></svg>
        555-318-4927
      </p>
      <p class="contact__line">
        <svg viewBox="0 0 24 24" aria-hidden="true"><path fill="#e3313a" d="M2 5h20v14H2z"/><path fill="none" stroke="#fff" stroke-width="2" d="M3 6l9 7 9-7"/></svg>
        info@heronaccord-example.org
      </p>
    </div>
    <div class="footer-band" role="img" aria-label="Decorative red and gold flowing band along the bottom edge"></div>
    <p class="website">www.heronaccord-example.org</p>
  </section>

  <section class="card card--back">
    <div class="back-copy">
      <p>Got Conflict? Try Conflict Coaching.</p>
      <p>Initial consultation is complimentary</p>
      <div class="social">
        <span class="social__rule social__rule--left"></span>
        <span class="social__badge"></span>
        <span class="social__badge"></span>
        <span class="social__rule social__rule--right"></span>
      </div>
      <p class="slogan">Finding Calm Around the Room<sup>®</sup></p>
    </div>
  </section>
</body>
</html>
```